I need a business card.

I need a simple, minimalist, business card. I think the coolest business card I have ever seen is Marty Vexler's from Kestrel's 9... it is just a little creepy for the real world.
I am a photographer and I need a card that I can give to brides or potential portrait customers that is simple and classy.
My name is Glen Hardesty. My website is www.glenhardesty-example.com
Please design my card.
I think it could be as simple as my name, phone # and website... where the rest of my contact could be found... or maybe my email and no website... I am open to ideas. I imagined the card on thick card stock with a black background...

```html
<!DOCTYPE html>
<html lang="en">
<head>
<meta charset="utf-8">
<title>Glen Hardesty – Business Card</title>
<link rel="stylesheet" href="https://fonts.googleapis.com/css2?family=Raleway:wght@200;300&family=Questrial&display=swap">
<style>
  :root {
    --page: #ffffff;
    --card: #000000;
    --paper: #ffffff;
    --paper-edge: #d9d9d9;
    --ink: #ffffff;
    --label: #111111;
    --fade: #5a5a5a;
  }
  html, body {
    margin: 0;
    padding: 0;
    width: 1200px;
    height: 873px;
    overflow: hidden;
    background: var(--page);
  }
  .sheet {
    position: relative;
    width: 1200px;
    height: 873px;
  }
  .card {
    position: absolute;
    background: var(--card);
    box-shadow: 3px 4px 5px rgba(0,0,0,0.45);
  }
  .card svg { display: block; width: 100%; height: 100%; }
  .card--front { left: 45px; top: 38px; width: 545px; height: 280px; }
  .card--back { left: 637px; top: 38px; width: 494px; height: 280px; }
  .card--single { left: 277px; top: 456px; width: 627px; height: 353px; }
  .caption {
    position: absolute;
    font-family: "Questrial", sans-serif;
    font-size: 24px;
    color: var(--label);
    transform: translateX(-50%);
    margin: 0;
  }
  .caption--front { left: 292px; top: 328px; }
  .caption--back { left: 896px; top: 326px; }
  .caption--single { left: 588px; top: 822px; }
  .name-display { font-family: "Raleway", sans-serif; font-weight: 200; }
  .detail { font-family: "Questrial", sans-serif; fill: var(--ink); }
</style>
</head>
<body>
<main class="sheet">

  <!-- Front -->
  <section class="card card--front" aria-label="Card front">
    <svg viewBox="0 0 500 257" xmlns="http://www.w3.org/2000/svg">
      <defs>
        <linearGradient id="nameFade" x1="0" y1="0" x2="0" y2="1">
          <stop offset="0" stop-color="#ffffff"/>
          <stop offset="1" stop-color="#3a3a3a"/>
        </linearGradient>
        <filter id="printShadow" x="-20%" y="-20%" width="140%" height="140%">
          <feDropShadow dx="2" dy="3" stdDeviation="3" flood-color="#000" flood-opacity="0.6"/>
        </filter>
      </defs>
      <text class="name-display" x="66" y="116" font-size="62" fill="url(#nameFade)">Glen Hardesty</text>
      <g class="print-stack">
        <g transform="translate(238 135) rotate(6)" filter="url(#printShadow)">
          <rect x="-100" y="-105" width="200" height="210" fill="var(--paper)"/>
        </g>
        <g transform="translate(222 140) rotate(-3)" filter="url(#printShadow)">
          <rect x="-100" y="-105" width="200" height="210" fill="var(--paper)"/>
          <rect x="-92" y="-97" width="184" height="150" fill="var(--card)"/>
        </g>
        <g transform="translate(232 122) rotate(-8)" filter="url(#printShadow)">
          <rect x="-106" y="-108" width="212" height="218" fill="var(--paper)"/>
          <rect x="-98" y="-100" width="196" height="160" fill="var(--card)"/>
        </g>
      </g>
      <text class="name-display" x="66" y="116" font-size="62" fill="url(#nameFade)" opacity="0.55">Glen Hardesty</text>
      <text class="detail" x="354" y="220" font-size="17">Photographer</text>
      <line x1="352" y1="226" x2="496" y2="226" stroke="var(--ink)" stroke-width="1"/>
      <text class="detail" x="343" y="248" font-size="19">555.014.2277</text>
    </svg>
  </section>
  <p class="caption caption--front">front</p>

  <!-- Back -->
  <section class="card card--back" aria-label="Card back">
    <svg viewBox="0 0 453 257" xmlns="http://www.w3.org/2000/svg">
      <defs>
        <linearGradient id="urlFade" x1="0" y1="0" x2="0" y2="1">
          <stop offset="0" stop-color="#ffffff"/>
          <stop offset="1" stop-color="#444444"/>
        </linearGradient>
      </defs>
      <text class="name-display" x="226" y="124" font-size="27" text-anchor="middle" fill="url(#urlFade)">www.glenhardesty-example.com</text>
    </svg>
  </section>
  <p class="caption caption--back">back</p>

  <!-- One sided -->
  <section class="card card--single" aria-label="Single-sided card">
    <svg viewBox="0 0 575 324" xmlns="http://www.w3.org/2000/svg">
      <defs>
        <filter id="printShadowLg" x="-20%" y="-20%" width="140%" height="140%">
          <feDropShadow dx="3" dy="4" stdDeviation="4" flood-color="#000" flood-opacity="0.6"/>
        </filter>
      </defs>
      <rect class="edge-rule" x="3" y="6" width="3" height="310" fill="var(--paper)"/>
      <rect class="edge-rule" x="568" y="6" width="3" height="310" fill="var(--paper)"/>
      <g class="print-stack">
        <g transform="translate(275 140) rotate(6)" filter="url(#printShadowLg)">
          <rect x="-120" y="-135" width="240" height="270" fill="var(--paper)"/>
        </g>
        <g transform="translate(258 150) rotate(-3)" filter="url(#printShadowLg)">
          <rect x="-120" y="-135" width="240" height="270" fill="var(--paper)"/>
          <rect x="-110" y="-125" width="220" height="200" fill="var(--card)"/>
        </g>
        <g transform="translate(265 152) rotate(-10)" filter="url(#printShadowLg)">
          <rect x="-126" y="-140" width="252" height="284" fill="var(--paper)"/>
          <rect x="-115" y="-129" width="230" height="205" fill="var(--card)"/>
          <text class="detail" x="0" y="-18" font-size="30" text-anchor="middle">Glen Hardesty</text>
          <text class="detail" x="0" y="114" font-size="17" text-anchor="middle" fill="var(--card)" style="fill:var(--card)">www.glenhardesty-example.com</text>
        </g>
      </g>
      <text class="detail" x="411" y="114" font-size="21">Photographer</text>
      <text class="detail" x="403" y="180" font-size="22">555.014.2277</text>
    </svg>
  </section>
  <p class="caption caption--single">one sided</p>

</main>
</body>
</html>
```